Corporate Brochure Cover Design

We need a design for a corporate A4 Size portfolio cover (front and back) which we will be distributing. to our commercial clients.

We are a professional plumbing company that is an industry leader for service we provide to our clients and technology we use. The design needs to incorporate the colours black, red, white and silver and needs to include our logo. We dont have any slogans or mottos... If you wanted to use something it could be "Delivering exceptional service...Always!" however i dont want it to b the focal point of the cover.

Im looking for something professional and modern that has the WOW factor!

Size is A4 - both front and back covers. You can include pictures as well or sample pictures of where we can source and put our own team pictures.

if you have any questions, please do not hesitate to contact me.

Target Market(s)

Our commercial & strata clients - professional industry.

Industry/Entity Type

Commercial

Font styles to use
Sans Serif

Requirements
Must have
• Red, black, white, silver as the colour scheme.
• Include the logo.
Nice to have
• Modern design and something that makes the client go WOW before they open the brochure.
Should not have
• lots of text

```html
<!DOCTYPE html>
<html lang="en">
<head>
<meta charset="utf-8">
<title>Keystone Brochure Cover</title>
<link rel="stylesheet" href="https://fonts.googleapis.com/css2?family=Source+Sans+3:wght@300;400;600;700&display=swap">
<style>
  :root {
    --ink: #221f1f;
    --ink-soft: rgba(28, 25, 25, 0.64);
    --ink-faint: rgba(28, 25, 25, 0.40);
    --red: #d5202a;
    --white: #ffffff;
    --wood-deep: #3a2a1e;
    --wood-dark: #4e3a29;
    --wood-mid: #6a5038;
    --wood-light: #86674a;
    --tool-yellow: rgba(232, 200, 40, 0.30);
    --tool-orange: rgba(230, 96, 30, 0.26);
    --tool-red: rgba(200, 30, 30, 0.22);
    --tool-steel: rgba(190, 190, 185, 0.20);
  }
  html, body {
    margin: 0;
    padding: 0;
    width: 1200px;
    height: 897px;
    overflow: hidden;
    background: #e6e6e6;
    font-family: "Source Sans 3", "Myriad Pro", sans-serif;
  }
  .spread {
    position: relative;
    width: 1200px;
    height: 897px;
    overflow: hidden;
  }
  .photo {
    position: absolute;
    inset: 0;
    background:
      radial-gradient(ellipse 120px 100px at 265px 345px, var(--tool-yellow), transparent 70%),
      radial-gradient(ellipse 110px 90px at 330px 760px, var(--tool-yellow), transparent 70%),
      radial-gradient(ellipse 110px 120px at 1070px 620px, var(--tool-yellow), transparent 70%),
      radial-gradient(ellipse 120px 80px at 430px 290px, var(--tool-orange), transparent 70%),
      radial-gradient(ellipse 130px 80px at 160px 790px, var(--tool-orange), transparent 70%),
      radial-gradient(ellipse 140px 110px at 720px 360px, var(--tool-red), transparent 70%),
      radial-gradient(ellipse 150px 120px at 520px 590px, var(--tool-steel), transparent 70%),
      radial-gradient(ellipse 120px 120px at 770px 160px, var(--tool-steel), transparent 70%),
      radial-gradient(ellipse at 50% 45%, rgba(140, 108, 74, 0.45), transparent 65%),
      linear-gradient(180deg, var(--wood-dark) 0%, var(--wood-mid) 30%, var(--wood-light) 50%, var(--wood-mid) 75%, var(--wood-deep) 100%);
  }
  .fold {
    position: absolute;
    left: 599px;
    top: 0;
    width: 2px;
    height: 897px;
    background: linear-gradient(90deg, rgba(0,0,0,0.12), rgba(255,255,255,0.06));
  }
  .tile { position: absolute; }
  .tile--soft { background: var(--ink-soft); }
  .tile--faint { background: var(--ink-faint); }
  .tile--solid { background: var(--ink); }
  .tile--red { background: var(--red); }

  .card {
    position: absolute;
    width: 215px;
    height: 228px;
    background: var(--ink);
    color: var(--white);
    text-align: center;
  }
  .card--contact { left: 192px; top: 334px; }
  .card--brand { left: 793px; top: 333px; }

  .wordmark {
    display: inline-flex;
    align-items: center;
    gap: 6px;
    font-weight: 700;
    color: var(--white);
    letter-spacing: 0.5px;
  }
  .wordmark__dot {
    width: 10px;
    height: 10px;
    border-radius: 50%;
    background: var(--red);
  }
  .card--contact .wordmark { margin-top: 40px; font-size: 25px; }
  .card--brand .wordmark { margin-top: 96px; font-size: 28px; }

  .card__name {
    margin-top: 36px;
    font-size: 17px;
    font-weight: 400;
    line-height: 1;
  }
  .card__tagline {
    margin-top: 5px;
    font-size: 9.5px;
    line-height: 1;
  }
  .card__phone {
    margin-top: 24px;
    font-size: 13px;
  }
  .card__email {
    margin-top: 8px;
    font-size: 13px;
  }

  .slogan {
    position: absolute;
    left: 984px;
    top: 623px;
    width: 108px;
    height: 114px;
    background: var(--red);
    color: var(--white);
    box-sizing: border-box;
    padding: 14px 8px 0 11px;
    font-size: 17px;
    font-weight: 300;
    line-height: 1.12;
  }
  .slogan__end { display: block; text-align: right; }

  .promise {
    position: absolute;
    left: 779px;
    top: 762px;
    color: var(--white);
  }
  .promise__hours {
    font-size: 38px;
    font-weight: 400;
    line-height: 1;
  }
  .promise__label {
    font-size: 16px;
    font-weight: 400;
    margin-top: 4px;
  }
</style>
</head>
<body>
<div class="spread">
  <div class="photo" role="img" aria-label="Photograph of plumbing and hand tools laid out on a rustic wooden workbench: yellow tape measures, orange and red handled pliers, adjustable wrench, screwdrivers, spirit level, caliper, gears and bearing"></div>
  <div class="fold"></div>

  <div class="tile tile--soft" style="left:0;top:0;width:407px;height:97px"></div>
  <div class="tile tile--faint" style="left:0;top:97px;width:190px;height:120px"></div>
  <div class="tile tile--soft" style="left:84px;top:217px;width:106px;height:111px"></div>
  <div class="tile tile--faint" style="left:0;top:328px;width:84px;height:114px"></div>

  <div class="tile tile--faint" style="left:984px;top:0;width:216px;height:97px"></div>
  <div class="tile tile--soft" style="left:1092px;top:97px;width:108px;height:114px"></div>

  <div class="tile tile--solid" style="left:1092px;top:509px;width:108px;height:114px"></div>
  <div class="tile tile--solid" style="left:1092px;top:623px;width:108px;height:114px"></div>

  <div class="tile tile--solid" style="left:765px;top:737px;width:109px;height:160px"></div>
  <div class="tile tile--soft" style="left:874px;top:737px;width:110px;height:116px"></div>
  <div class="tile tile--red" style="left:874px;top:853px;width:110px;height:44px"></div>
  <div class="tile tile--solid" style="left:984px;top:737px;width:108px;height:160px"></div>
  <div class="tile tile--soft" style="left:1092px;top:737px;width:108px;height:160px"></div>

  <div class="card card--contact">
    <div class="wordmark"><span class="wordmark__dot"></span>KEYSTONE</div>
    <div class="card__name">KEYSTONE</div>
    <div class="card__tagline">PLUMBING &amp; HOME SERVICE PROFESSIONALS</div>
    <div class="card__phone">T. 088 41 209</div>
    <div class="card__email">info@keystoneplumbing.com</div>
  </div>

  <div class="card card--brand">
    <div class="wordmark"><span class="wordmark__dot"></span>KEYSTONE</div>
  </div>

  <div class="slogan">Delivering exceptional service... <span class="slogan__end">Always!</span></div>

  <div class="promise">
    <div class="promise__hours">24/7</div>
    <div class="promise__label">guaranteed</div>
  </div>
</div>
</body>
</html>
```